Lena Corvell Business Card

I need a business card that reflects my current website: itslenacorvell.example and screenshot attached. If we keep the color scheme of the site and sample card below that would be ideal. The business card should include the information on the attached sample cards.

Industry/Entity Type

Business

```html
<!DOCTYPE html>
<html lang="en">
<head>
<meta charset="utf-8">
<title>Lena Corvell – Business Card</title>
<link rel="stylesheet" href="https://fonts.googleapis.com/css2?family=Roboto:wght@300;400&display=swap">
<style>
  :root {
    --paper: #f2f2f2;
    --teal: #5fb8a8;
    --teal-soft: #79c9bb;
    --bubble: #dcecea;
    --slate: #555a63;
    --ink: #3d3f44;
    --ink-soft: #4a4c52;
    --white: #ffffff;
  }
  html, body {
    margin: 0;
    padding: 0;
    overflow: hidden;
    background: var(--paper);
  }
  .card {
    position: relative;
    width: 1200px;
    height: 753px;
    background: var(--paper);
    overflow: hidden;
    font-family: "Roboto", Arial, sans-serif;
    color: var(--ink);
  }
  .wordmark {
    position: absolute;
    top: 98px;
    left: 0;
    width: 1200px;
    text-align: center;
    font-size: 40px;
    font-weight: 300;
    color: #111111;
    letter-spacing: 0.01em;
  }
  .decor {
    position: absolute;
    top: 0;
    left: 0;
  }
  .name {
    position: absolute;
    left: 36px;
    top: 536px;
    margin: 0;
    font-size: 48px;
    font-weight: 400;
    letter-spacing: 0.2em;
    color: var(--slate);
    white-space: nowrap;
  }
  .name .surname { color: var(--teal); }
  .tagline {
    position: absolute;
    left: 37px;
    top: 597px;
    margin: 0;
    font-size: 17px;
    font-weight: 400;
    color: var(--ink-soft);
    letter-spacing: 0.01em;
  }
  .contacts {
    position: absolute;
    left: 772px;
    top: 503px;
    margin: 0;
    padding: 0;
    list-style: none;
  }
  .contacts li {
    display: flex;
    align-items: center;
    height: 41px;
    font-size: 20px;
    font-weight: 400;
    color: var(--ink-soft);
  }
  .contacts .icon {
    width: 28px;
    height: 22px;
    margin-right: 23px;
    display: flex;
    justify-content: center;
    align-items: center;
    color: #111111;
  }
  .contacts .at-sign {
    font-size: 19px;
    font-weight: 400;
  }
</style>
</head>
<body>
<main class="card">
  <div class="wordmark">its Lena Corvell</div>

  <svg class="decor" width="1200" height="753" viewBox="0 0 1200 753" aria-hidden="true">
    <circle cx="735" cy="276" r="61" fill="var(--bubble)" opacity="0.9"/>
    <circle cx="653" cy="245" r="37" fill="#e3f1ef"/>
    <rect x="0" y="321" width="1200" height="88" fill="var(--white)"/>
    <rect x="0" y="324" width="1200" height="82" fill="var(--teal)"/>
    <rect x="0" y="362" width="1200" height="6" fill="var(--slate)"/>
    <circle cx="496" cy="441" r="64" fill="var(--bubble)" opacity="0.9"/>
    <circle cx="563" cy="480" r="39" fill="#e3f1ef"/>
    <defs>
      <radialGradient id="portraitTone" cx="50%" cy="45%" r="55%">
        <stop offset="0%" stop-color="#8a4a2a"/>
        <stop offset="55%" stop-color="#6a3a24"/>
        <stop offset="100%" stop-color="var(--teal-soft)"/>
      </radialGradient>
    </defs>
    <circle cx="615" cy="359" r="110" fill="var(--white)"/>
    <circle cx="615" cy="359" r="105" fill="url(#portraitTone)" role="img" aria-label="Portrait photo of Lena Corvell on a teal background"/>
  </svg>

  <h1 class="name">LENA <span class="surname">CORVELL</span></h1>
  <p class="tagline">Brand Curator | Digital Storyteller | Social Entrpreneur</p>

  <ul class="contacts">
    <li>
      <span class="icon">
        <svg width="20" height="14" viewBox="0 0 20 14" aria-hidden="true">
          <rect x="0" y="0" width="20" height="14" fill="#111"/>
          <path d="M0 0 L10 8 L20 0" fill="none" stroke="var(--paper)" stroke-width="1.6"/>
          <path d="M0 14 L7 6.5 M20 14 L13 6.5" stroke="var(--paper)" stroke-width="1.2"/>
        </svg>
      </span>
      me@lenacorvell.example
    </li>
    <li>
      <span class="icon">
        <svg width="13" height="21" viewBox="0 0 13 21" aria-hidden="true">
          <rect x="0.9" y="0.9" width="11.2" height="19.2" rx="1.8" fill="none" stroke="#111" stroke-width="1.8"/>
          <rect x="2.8" y="3.2" width="7.4" height="11.5" fill="#111"/>
          <circle cx="6.5" cy="17.3" r="1.1" fill="#111"/>
        </svg>
      </span>
      555.010.4821
    </li>
    <li>
      <span class="icon"><span class="at-sign">@</span></span>
      [fb] | [t.] | [ig] @itslenacorvell
    </li>
    <li>
      <span class="icon">
        <svg width="19" height="19" viewBox="0 0 20 20" aria-hidden="true">
          <g fill="none" stroke="#111" stroke-width="1.4">
            <circle cx="10" cy="10" r="8.6"/>
            <ellipse cx="10" cy="10" rx="3.8" ry="8.6"/>
            <line x1="1.4" y1="10" x2="18.6" y2="10"/>
            <path d="M3 5.3 H17 M3 14.7 H17"/>
            <line x1="10" y1="1.4" x2="10" y2="18.6"/>
          </g>
        </svg>
      </span>
      www.itslenacorvell.example
    </li>
  </ul>
</main>
</body>
</html>
```